New Energy Drink

*Name, Logo, Flatlay, and V5 Mockup design of a new energy drink*
We are a current RTD (ready to drink) company looking to expand into the Energy market. We are not sure if we will stick with our parent company name or go a completely different direction. That's where you come in.
Get creative. Come up with a name, design a logo, and create the look and feel of our next big product. We want fun, bright, and forward-thinking designs. Don't think Zipfox and tundra, but more along the lines of Crane, V5, and Tilt as our proposed target market is in the same 18-25 demographic.
The only request is the Term "With Super Caffeine" appear somewhere on the visible label. A V5 can render is attached. Please provide a Lay Flat and a Rendered Can together when submitting your designs.
FYI, the design brief is just a generic template. DO NOT USE the "grunge" or "brick" as a reference when creating your designs. We are offering a $1,000 prize to the winning designer. So please, really think this through. 1 great design is better than 5 quick designs. Good Luck!
18-25

```html
<!DOCTYPE html>
<html lang="en">
<head>
<meta charset="UTF-8">
<title>Do It Energy Drink – Label Lay Flat</title>
<link rel="stylesheet" href="https://fonts.googleapis.com/css2?family=Nunito:wght@600;800;900&family=Roboto:wght@500;700&display=swap">
<style>
  :root {
    --sky: #0dbde8;
    --cream: #f3efe4;
    --lemon: #d8d21c;
    --berry: #c8124e;
    --ocean: #2a8fbf;
    --ocean-bright: #1f9fd6;
    --tangerine: #ee8a3c;
    --tangerine-dark: #e4772c;
    --white: #ffffff;
  }
  html, body {
    margin: 0;
    padding: 0;
    width: 1200px;
    height: 1000px;
    overflow: hidden;
    background: var(--sky);
  }
  .canvas { display: block; width: 1200px; height: 1000px; }
  .label-cream { fill: var(--cream); }
  .label-lemon { fill: var(--lemon); }
  .label-berry { fill: var(--berry); }
  .caffeine-disc { fill: var(--tangerine); }
  .caffeine-ring-text {
    fill: var(--tangerine-dark);
    font-family: "Roboto", Arial, sans-serif;
    font-weight: 500;
    font-size: 15px;
    letter-spacing: 2px;
  }
  .brand-name {
    fill: var(--ocean);
    font-family: "Nunito", Arial, sans-serif;
    font-weight: 800;
    font-size: 160px;
    letter-spacing: 2px;
  }
  .tagline {
    fill: var(--ocean-bright);
    font-family: "Roboto", Arial, sans-serif;
    font-weight: 700;
    font-size: 14px;
  }
  .product-type {
    fill: var(--white);
    font-family: "Roboto", Arial, sans-serif;
    font-weight: 700;
    font-size: 24px;
  }
  .volume {
    fill: var(--white);
    font-family: "Roboto", Arial, sans-serif;
    font-weight: 500;
    font-size: 13px;
  }
</style>
</head>
<body>
<svg class="canvas" viewBox="0 0 1200 1000" xmlns="http://www.w3.org/2000/svg">
  <defs>
    <clipPath id="label-clip">
      <rect x="445" y="110" width="310" height="760"/>
    </clipPath>
    <path id="caffeine-arc" d="M 542 262 A 64 64 0 1 1 658 262"/>
  </defs>

  <g class="label" clip-path="url(#label-clip)">
    <rect class="label-lemon" x="445" y="110" width="310" height="760"/>
    <path class="label-cream" d="M 445 110 H 755 V 250 Q 600 290 445 250 Z"/>
    <path class="label-berry" d="M 445 870 V 790 Q 445 715 600 715 Q 755 715 755 790 V 870 Z"/>
  </g>

  <g class="caffeine-badge">
    <circle class="caffeine-disc" cx="600" cy="222" r="40"/>
    <text class="caffeine-ring-text">
      <textPath href="#caffeine-arc" startOffset="50%" text-anchor="middle">WITH SUPER CAFFEINE</textPath>
    </text>
  </g>

  <g class="brand-lockup">
    <text class="brand-name" x="600" y="490" text-anchor="middle">DO</text>
    <text class="brand-name" x="600" y="670" text-anchor="middle">IT</text>
    <text class="tagline" x="594" y="510" text-anchor="middle">MAKE</text>
    <text class="tagline" x="594" y="526" text-anchor="middle">YOUR</text>
    <text class="tagline" x="594" y="542" text-anchor="middle">DAY!</text>
  </g>

  <g class="product-info">
    <text class="product-type" x="600" y="792" text-anchor="middle">ENERGY DRINK</text>
    <text class="volume" x="600" y="812" text-anchor="middle">16 FL OZ (273ML)</text>
  </g>
</svg>
</body>
</html>
```